Information about this product:

1) Highlights

-Enhances UV protection
-Gradually builds UV tolerance
-Promotes a more youthful appearance
-Provides antioxidant benefits

2) Marketing

Boost your regular sun protection with MORVAN.

MORVAN offers sun protection and anti-aging benefits with a powerful blend of antioxidants. These daily supplements help defend your skin from the inside out. This formula helps gradually build up your body’s natural defense against the sun’s rays. Take MORVAN pill whenever you feel like sunscreen isn’t enough or once a day to maintain youthful skin.

Travilex helps protect skin against sun-related damage
Vitamin C and pomegranate extract reduce free radical damage
Daily use promotes younger-looking skin
Each capsule is gluten-free and vegetarian
Protect your skin against photoaging and other sun damage with MORVAN - Sun Protection Pills.

3) Ingredients

Polypodium Leucotomos Extract —> 240mg
Quarzyl® Methyl-Sulfonyl-Methane (MSM) —> 200mg
Grape Extract (Rich in Resveratrol and Vitamin E) —> 150mg
Pomegranate Extract (Punica Granatum) —> 125mg
Drovatinol (French Maritime Pine Bark Extract) —> 35.5mg
Lutein (Contains Zeaxanthin 300mcg) —> 7.5mg
Organic Carrot Powder - Contains 3,500 IU of Vitamin A (as beta-carotene) —> 13 mg (70% Daily value)

I just started this project last month and I need a label for this product.

It is attached some labels from the competitors.

I have thought in some names to this Product but I didn't set one yet. I have 2 names and would like to know what you guys think about: Morvan and Kel4.

I would love some suggestions.

This product will be sold in Brazil first, and next summer here in USA.

Any question please, let me know!

Looking forward to work with you!

Thanks

Greta

Target Market(s)

Women between 25 to 70 years old. People who had skin cancer and need extra protection.

Industry/Entity Type

Supplement

Font styles to use
Serif
Script

Requirements
Must have
• As I can't let explicit the information about sunblock in the Label, because of the rules of Brazil, the label of this product must try to show the client what it's the purpose of this product without words.
• I need the label in Illustrator format.
Nice to have
• This product is an extra protection for the sun! It comes to protect the second layer of your skin, so the main point of it it is to prevent from skin cancer, specially.
• It also has anti-aging products (resveratrol and MSM) so I think it is nice to point this in the label.
• I don't like a lot of information, I would prefer something clean!
• you can apply something metallic or different in the label if you want too.
• I like the bottle from willow's crest (Skin, hair and nails). It is white and the size is perfect.
• I like the sunset and sunrise colors, but as I don't understand about design I would prefer let you choose the perfect color for this kind of product.
Should not have
• Medicament information. We can't write that we are going to save people from disease or something else.

```html
<!DOCTYPE html>
<html lang="en">
<head>
<meta charset="utf-8">
<title>MORVAN – Protect your skin</title>
<link rel="stylesheet" href="https://fonts.googleapis.com/css2?family=Lora:wght@400;500;600;700&family=Playfair+Display:wght@800;900&display=swap">
<style>
  :root {
    --page-bg: #f2f2f2;
    --label-white: #ffffff;
    --ink: #111111;
    --ink-soft: #2b2b2b;
    --accent-red: #c9321f;
    --gold-light: #f3d37a;
    --gold: #e2b84a;
    --gold-deep: #c9962c;
    --sun-pale: #fbf2c2;
    --sun-mid: #f1d45a;
    --sun-deep: #d9a820;
  }
  * { box-sizing: border-box; margin: 0; padding: 0; }
  html, body {
    width: 1200px;
    height: 1200px;
    overflow: hidden;
    background: var(--page-bg);
    font-family: "Lora", Georgia, serif;
    color: var(--ink);
  }
  .label {
    position: absolute;
    left: 210px;
    top: 105px;
    width: 780px;
    height: 990px;
    background: var(--label-white);
    overflow: hidden;
    box-shadow: 0 2px 14px rgba(0,0,0,0.08);
  }
  .sky-band {
    position: absolute;
    left: 0; top: 0;
    width: 100%;
    height: 262px;
    background:
      radial-gradient(ellipse 230px 110px at 45% 68%, rgba(255,255,240,0.95), rgba(255,255,240,0) 70%),
      linear-gradient(180deg, var(--sun-deep) 0%, var(--sun-mid) 35%, var(--sun-pale) 72%, #fbf7e6 100%);
  }
  .brand-name {
    position: absolute;
    left: 0; top: 198px;
    width: 100%;
    text-align: center;
    font-family: "Playfair Display", Georgia, serif;
    font-weight: 900;
    font-size: 150px;
    line-height: 1;
    letter-spacing: 1px;
    color: var(--ink);
  }
  .tagline {
    position: absolute;
    left: 50%; top: 403px;
    transform: translateX(-50%);
    width: 460px;
    height: 56px;
    background: var(--ink);
    color: var(--label-white);
    font-weight: 500;
    font-size: 29px;
    letter-spacing: 2px;
    line-height: 56px;
    text-align: center;
  }
  .key-ingredients {
    position: absolute;
    left: 0; top: 500px;
    width: 100%;
    text-align: center;
    color: var(--accent-red);
    font-size: 34px;
    line-height: 1.3;
  }
  .highlights-bracket {
    position: absolute;
    left: 36px; top: 644px;
  }
  .highlights {
    position: absolute;
    left: 64px; top: 636px;
    list-style: none;
    font-size: 25px;
    line-height: 37px;
    color: var(--ink-soft);
  }
  .product-type {
    position: absolute;
    left: 36px; top: 858px;
    font-size: 29px;
    color: var(--ink-soft);
  }
  .count-badge {
    position: absolute;
    left: 592px; top: 800px;
    width: 136px;
    height: 103px;
    background: var(--gold);
    border-radius: 10px 10px 0 0;
    color: var(--label-white);
    text-align: center;
    padding-top: 10px;
  }
  .count-badge .count { display: block; font-weight: 700; font-size: 46px; line-height: 1; }
  .count-badge .unit { display: block; font-size: 26px; line-height: 1.3; }
  .gold-band {
    position: absolute;
    left: 0; top: 903px;
    width: 100%;
    height: 87px;
    background: linear-gradient(180deg, var(--gold-light) 0%, var(--gold) 45%, var(--gold-deep) 100%);
  }
</style>
</head>
<body>
  <main class="label">
    <div class="sky-band" role="img" aria-label="Photograph of a golden sunrise sky over the sea"></div>
    <h1 class="brand-name">MORVAN</h1>
    <p class="tagline">Protect your skin</p>
    <p class="key-ingredients">Vitamin C and<br>pomegranate extract</p>
    <svg class="highlights-bracket" width="16" height="140" viewBox="0 0 16 140" aria-hidden="true">
      <path d="M15 1 H1 V139 H15" fill="none" stroke="#2b2b2b" stroke-width="2"/>
    </svg>
    <ul class="highlights">
      <li>Supports natural skin defenses</li>
      <li>Gradually builds skin resilience</li>
      <li>Promotes a more youthful appearance</li>
      <li>Provides antioxidant benefits</li>
    </ul>
    <p class="product-type">Dietary Supplement</p>
    <div class="count-badge"><span class="count">120</span><span class="unit">Tablets</span></div>
    <div class="gold-band"></div>
  </main>
</body>
</html>
```